Graphic Design Needed for Powerpoint Deck

We need a powerpoint design template, font, and look and feel for a new company called Meadow Wellness. Specific needs are listed in the attached file and if we like what we see we will more than likely use you in the future.
We like warm natural colors from a branding point of view, greens, browns, etc.
Target Market(s)
This will be used with potential investors and business partners.
Industry/Entity Type
Graphic Design
Requirements
Must have
- Graphic Designs for the charts mentioned in the powerpoint
- Overall Look and Feel
Nice to have
- Custom Font recommendations (Trebuchet is the one we like the most that is standard)

```html
<!DOCTYPE html>
<html lang="en">
<head>
<meta charset="utf-8">
<title>Meadow Wellness – The problem</title>
<link rel="stylesheet" href="https://fonts.googleapis.com/css2?family=PT+Sans:wght@400;700&display=swap">
<style>
  :root {
    --green-title: #17a04a;
    --green-bright: #00f000;
    --green-edge: #3ff23a;
    --green-pale: #e9fbe9;
    --map-green: rgba(95, 215, 122, 0.75);
    --map-green-fade: rgba(95, 215, 122, 0);
    --tan: #dfa672;
    --red: #ee1111;
    --ink: #111111;
    --white: #ffffff;
  }
  html, body {
    margin: 0;
    padding: 0;
    overflow: hidden;
    background: var(--white);
  }
  .slide {
    position: relative;
    width: 1200px;
    height: 900px;
    overflow: hidden;
    font-family: "PT Sans", "Trebuchet MS", sans-serif;
    background: linear-gradient(90deg, var(--white) 0%, var(--green-pale) 38%, #b4f5b0 62%, var(--green-edge) 100%);
  }
  .slide-title {
    position: absolute;
    left: 90px;
    top: 70px;
    margin: 0;
    font-size: 56px;
    font-weight: 700;
    color: var(--green-title);
    letter-spacing: 1.5px;
  }
  .region-map {
    position: absolute;
    left: 470px;
    top: 180px;
    width: 730px;
    height: 720px;
    background: radial-gradient(ellipse 75% 70% at 70% 55%, var(--map-green) 0%, var(--map-green) 55%, var(--map-green-fade) 100%);
  }
  .brand-badge {
    position: absolute;
    left: 998px;
    top: 45px;
    width: 166px;
    height: 166px;
    border-radius: 50%;
    background: var(--white);
    border: 14px solid var(--tan);
    box-sizing: border-box;
    display: flex;
    align-items: center;
    justify-content: center;
    text-align: center;
    box-shadow: 0 6px 16px rgba(0,0,0,0.25);
  }
  .brand-name {
    font-size: 22px;
    font-weight: 700;
    line-height: 1.1;
    color: var(--ink);
  }
  .stat-statement {
    position: absolute;
    left: 147px;
    top: 440px;
    margin: 0;
    font-size: 46px;
    line-height: 52px;
    letter-spacing: 1.5px;
    color: var(--ink);
  }
  .stat-statement .highlight {
    color: var(--red);
    font-weight: 700;
  }
  .stat-donut {
    position: absolute;
    left: 740px;
    top: 338px;
    width: 326px;
    height: 326px;
  }
  .donut-label {
    font-family: "PT Sans", "Trebuchet MS", sans-serif;
    font-size: 66px;
    font-weight: 700;
    letter-spacing: 2px;
    fill: var(--green-title);
  }
</style>
</head>
<body>
  <main class="slide">
    <h1 class="slide-title">The problem…</h1>

    <div class="region-map" role="img" aria-label="Map of North America"></div>

    <div class="brand-badge">
      <span class="brand-name">Meadow<br>Wellness</span>
    </div>

    <p class="stat-statement">
      <span class="highlight">66.3%</span> of Americans<br>
      are <span class="highlight">overweight</span>
    </p>

    <svg class="stat-donut" viewBox="0 0 326 326" aria-label="Donut chart: 66.3%">
      <defs>
        <filter id="inner-shadow" x="-20%" y="-20%" width="140%" height="140%">
          <feDropShadow dx="0" dy="4" stdDeviation="6" flood-color="#000" flood-opacity="0.3"/>
        </filter>
      </defs>
      <circle cx="163" cy="163" r="130" fill="none" stroke="var(--tan)" stroke-width="46"/>
      <circle cx="163" cy="163" r="130" fill="none" stroke="var(--green-bright)" stroke-width="46"
        stroke-dasharray="440 817" transform="rotate(-98 163 163)"/>
      <circle cx="163" cy="163" r="107" fill="var(--white)" filter="url(#inner-shadow)"/>
      <text class="donut-label" x="163" y="186" text-anchor="middle">66.3%</text>
    </svg>
  </main>
</body>
</html>
```